Website for new dental office

I am Dr. Colin Marsh and am building a new dental practice. I specialize in general dentistry. I am young and have a higher end dental practice incorporating very new technologies and would like my website to reflect that. As many dental patients are older, the website must be very easy to navigate. I would like patients to be able to request appointments, and will eventually add on patient information forms (the health history, etc, that you normally fill out in the practice) from my practice management software, so leave an area for that.

Industry/Entity Type

Building

```html
<!DOCTYPE html>
<html lang="en">
<head>
<meta charset="utf-8">
<title>Marsh Dental</title>
<link href="https://fonts.googleapis.com/css2?family=Questrial&family=Open+Sans:wght@400;600&display=swap" rel="stylesheet">
<style>
:root{
  --blue:#1560a0;
  --blue-dark:#10528c;
  --navy:#124f86;
  --ink:#333;
  --muted:#888;
  --contact-bg:#ebebeb;
  --footer:#4a4a4a;
  --footer-text:#e2e2e2;
  --bar:#154f86;
  --white:#fff;
}
*{box-sizing:border-box;margin:0;padding:0}
html,body{width:932px;height:1200px;overflow:hidden;background:var(--white)}
body{position:relative;font-family:"Questrial",sans-serif;color:var(--ink)}
h1,h2{font-weight:400}
.abs{position:absolute}

/* header */
.logo{left:156px;top:32px;font-size:28px;color:var(--blue)}
.nav{right:156px;top:43px;display:flex;gap:19px;font-family:"Open Sans",sans-serif;font-weight:600;font-size:9.5px;letter-spacing:.3px}
.nav a{color:#1577a8;text-decoration:none}
.nav a.active{color:var(--navy);border-bottom:1px solid var(--navy);padding-bottom:3px}

/* hero */
.hero-photo{left:110px;top:76px;width:340px;height:238px;border-radius:48% 48% 0 0/60% 60% 0 0;background:radial-gradient(ellipse at 50% 45%,#d9c3b0 0%,#e9e2dc 45%,#f4f6f9 75%,#fff 100%)}
.hero-title{left:498px;top:118px;width:290px;font-size:37px;line-height:38px;color:var(--blue);letter-spacing:-.3px}
.hero-sub{left:500px;top:200px;font-size:11px;color:#777}
.hero-sub span{color:var(--blue)}
.hero-text{left:502px;top:221px;width:272px;font-size:8px;line-height:10.5px;color:#999}

/* call band */
.band{left:0;top:314px;width:932px;height:74px}
.band-label{font-family:"Open Sans",sans-serif;font-size:8.5px;color:#b9d2ea;letter-spacing:.2px}
.band-value{color:var(--white);font-size:20px;margin-top:2px}
.appt{left:223px;top:336px}
.call{left:619px;top:336px}
.call .band-value{font-size:21px}

/* welcome */
.welcome-title{left:0;width:932px;top:414px;text-align:center;font-size:17px;color:#222}
.welcome-text{left:156px;width:620px;top:444px;text-align:center;font-size:8.4px;line-height:11.3px;color:#444}

/* services */
.services{left:0;top:502px;width:932px;height:224px;background:linear-gradient(#f4f4f4,#fafafa 60%,#fff)}
.services-title{left:0;width:932px;top:528px;text-align:center;font-size:17px;color:#222}
.service{top:584px;width:200px;text-align:center}
.service svg{display:block;margin:0 auto}
.service p{margin-top:18px;font-size:9.6px;color:var(--blue);letter-spacing:.1px;white-space:nowrap}

/* contact */
.contact{left:0;top:726px;width:932px;height:250px;background:var(--contact-bg);border-top:1px solid #dcdcdc}
.address{left:156px;top:790px;font-size:19px;line-height:22.4px;color:#333}
.address span{color:var(--blue)}
.map{left:466px;top:728px;width:310px;height:248px;background:linear-gradient(135deg,#e8e3d2 0%,#dedad0 40%,#cfd0cc 100%)}

/* footer */
.footer{left:0;top:976px;width:932px;height:192px;background:var(--footer)}
.f-col{top:996px;width:156px;color:var(--footer-text)}
.f-head{font-size:12.5px;padding-bottom:5px;border-bottom:2px solid #ddd}
.f-logo{margin-top:18px;font-size:25px;color:#a8a8a8}
.f-text{font-family:"Open Sans",sans-serif;font-size:7.6px;line-height:9.6px;margin-top:10px}
.post{font-family:"Open Sans",sans-serif;font-size:7.6px;line-height:9.6px;margin-top:10px}
.posts .post:first-of-type{margin-top:18px}
.field{width:165px;height:21px;background:var(--white);border:1px solid #bbb;margin-top:6px}
.submit{margin:8px 0 0 91px;width:74px;height:22px;background:var(--bar);color:var(--white);font-family:"Open Sans",sans-serif;font-weight:600;font-size:7.5px;line-height:22px;text-align:center}
.bottom{left:0;top:1168px;width:932px;height:32px;background:var(--bar);color:#cbd9e8;font-family:"Open Sans",sans-serif;font-size:8px;line-height:32px;padding-left:159px}
</style>
</head>
<body>

<div class="abs logo">Marsh Dental</div>
<nav class="abs nav">
  <a class="active">HOME</a><a>SERVICES</a><a>TERMS OF USE</a><a>ABOUT US</a><a>TESTIMONIALS</a><a>CONTACT US</a>
</nav>

<div class="abs hero-photo" role="img" aria-label="Smiling family of four, parents carrying two young daughters"></div>
<h1 class="abs hero-title">Solution to every dental problem</h1>
<p class="abs hero-sub">Patient come to us with a pain, but leave with a <span>SMILE!</span></p>
<p class="abs hero-text">Lorem ipsum dolor sit amet, consectetuer adipiscing elit, sed diam nonummy nibh euismod tincidunt ut laoreet dolore magna aliquam erat volutpat. Ut wisi enim ad minim veniam,</p>

<svg class="abs band" width="932" height="74" viewBox="0 0 932 74">
  <rect width="932" height="74" fill="#1560a0"/>
  <polygon points="505,0 932,0 932,74 445,74" fill="#124f86"/>
  <line x1="505" y1="0" x2="445" y2="74" stroke="#fff" stroke-width="1.5"/>
  <g fill="none" stroke="#3f7fb5" stroke-width="5" opacity=".7">
    <path d="M160 18h40v44h-40z"/>
    <path d="M178 46l24-28 8 7-24 28-10 3z"/>
  </g>
  <g fill="#3f79ad" opacity=".7">
    <path d="M531 36c0-16 62-16 62 0v6h-14v-8c-10-4-24-4-34 0v8h-14z"/>
    <circle cx="551" cy="44" r="3.5"/><circle cx="562" cy="44" r="3.5"/><circle cx="573" cy="44" r="3.5"/>
    <circle cx="551" cy="54" r="3.5"/><circle cx="562" cy="54" r="3.5"/><circle cx="573" cy="54" r="3.5"/>
    <circle cx="551" cy="64" r="3.5"/><circle cx="562" cy="64" r="3.5"/><circle cx="573" cy="64" r="3.5"/>
  </g>
</svg>
<div class="abs appt"><div class="band-label">GET OUR SERVICES</div><div class="band-value">Request Appointments</div></div>
<div class="abs call"><div class="band-label">CALL US TODAY</div><div class="band-value">0800-555-01-246</div></div>

<h2 class="abs welcome-title">WELCOME TO MARSH DENTAL</h2>
<p class="abs welcome-text">Lorem ipsum dolor sit amet, consectetuer adipiscing elit, sed diam nonummy nibh euismod tincidunt ut laoreet dolore magna aliquam erat volutpat. Ut wisi enim ad minim veniam, quis nostrud exerci tation ullamcorper suscipit lobortis nisl ut aliquip ex ea commodo consequat. Duis autem vel eum iriure dolor in hendrerit in vulputate velit esse molestie consequat.</p>

<div class="abs services"></div>
<h2 class="abs services-title">SERVICES</h2>

<div class="abs service" style="left:116px">
  <svg width="76" height="76" viewBox="0 0 76 76"><circle cx="38" cy="38" r="35" fill="#fff" stroke="#1560a0" stroke-width="4"/>
    <g fill="#1560a0"><path d="M26 22h8v2h-2v8l8 12a4 4 0 0 1-3 5H23a4 4 0 0 1-3-5l8-12v-8h-2z"/><path d="M44 20h8v2h-2v10l6 12a4 4 0 0 1-3 5h-10a4 4 0 0 1-3-5l6-12V22h-2z"/></g></svg>
  <p>CRYSTAL VENEERS - DENTAL</p>
</div>
<div class="abs service" style="left:284px">
  <svg width="76" height="76" viewBox="0 0 76 76"><circle cx="38" cy="38" r="35" fill="#fff" stroke="#1560a0" stroke-width="4"/>
    <path d="M32 24h12v4h-3v-1h-6v1h-3z M22 28h32v20H22z" fill="#1560a0"/><path d="M36 32h4v5h5v4h-5v5h-4v-5h-5v-4h5z" fill="#fff"/></svg>
  <p>DENTAL TREATMENT</p>
</div>
<div class="abs service" style="left:452px">
  <svg width="76" height="76" viewBox="0 0 76 76"><circle cx="38" cy="38" r="35" fill="#fff" stroke="#1560a0" stroke-width="4"/>
    <g fill="#1560a0"><path d="M28 50l14-26 5 3-14 26z"/><path d="M36 48l10-14 6 4-10 14z"/><rect x="42" y="20" width="5" height="8" transform="rotate(30 44 24)"/></g></svg>
  <p>HIGHLY QUALIFIED AND EXPERIENCED</p>
</div>
<div class="abs service" style="left:610px">
  <svg width="76" height="76" viewBox="0 0 76 76"><circle cx="38" cy="38" r="35" fill="#fff" stroke="#1560a0" stroke-width="4"/>
    <path d="M28 24c4-2 7 1 10 1s6-3 10-1c4 2 4 9 2 14-2 4-2 14-5 14-3 0-3-10-7-10s-4 10-7 10c-3 0-3-10-5-14-2-5-2-12 2-14z" fill="#1560a0"/></svg>
  <p>PROBLEMS &amp; ORAL SURGERY</p>
</div>

<div class="abs contact"></div>
<div class="abs address">Dummy street<br>02-212 Dummy<br>information: <span>+48 700 555 013</span><br>appointments: <span>+48 800 555 0199</span><br>email: <span>frontdesk@marshdental.com</span></div>
<div class="abs map" role="img" aria-label="Street map showing the practice location"></div>

<div class="abs footer"></div>
<div class="abs f-col" style="left:155px">
  <div class="f-head">ABOUT US</div>
  <div class="f-logo">Marsh Dental</div>
  <p class="f-text">Dr. Colin Marsh auctor, nisi elit consequat ipsum, nec sagittis sem nibh id elit. Duis sed odio sit amet nibh vulputateUpdate: Website Theme Submission Requirements</p>
</div>
<div class="abs f-col posts" style="left:382px">
  <div class="f-head">LATEST POSTS</div>
  <p class="post">Update: Website Theme Submission Requirements</p>
  <p class="post">Does a well designed thumbnail increase your sales?</p>
  <p class="post">Brain Most Wanted - $5,000 Reward for the First 15 Hosting</p>
  <p class="post">Update: Website Theme Submission Requirements</p>
</div>
<div class="abs f-col" style="left:616px;width:158px">
  <div class="f-head">NEWSLETTER</div>
  <p class="post" style="margin-top:18px">Dr. Colin Marsh auctor, nisi elit consequat ipsum, nec sagittis sem nibh id</p>
  <div class="field" style="margin-left:-3px"></div>
  <div class="field" style="margin-left:-3px"></div>
  <div class="submit">SUBMIT NOW</div>
</div>
<div class="abs bottom">© 2013 Clinic Theme, All Rights Reserved.</div>

</body>
</html>
```